Harbor Kindness Inc

We need a full re-design of our non-profit organization website (www.harborkindness.org). Ideally, we are looking to make it more attractive, user-friendly, and interactive with our business model.

Please make sure to user colors that ago with our logo.

We need a homepage done and we also need a content page done where we will use for the other pages to fill with content.

Target Market(s)

Clothes/textiles donations.

Industry/Entity Type

Charity

Number of Pages Required

2 page

Colors

Designer to choose colors to be used in the design.

Requirements
Must have
• It must match the styling of our logo and same colors as current website. (www.harborkindness.org)
Nice to have
• Sleek homepage that is easy to understand and get our main points across.

```html
<!DOCTYPE html>
<html lang="en">
<head>
<meta charset="utf-8">
<title>Harbor Kindness – Home</title>
<link href="https://fonts.googleapis.com/css2?family=Raleway:wght@400;500;600;700;800&display=swap" rel="stylesheet">
<style>
:root{
  --red:#e8262d;
  --dark:#333333;
  --ink:#1d1d1d;
  --text:#333;
  --muted:#666;
  --light:#f4f4f4;
  --line:#e2e2e2;
  --green:#2e6b1d;
  --gold:#f2d77b;
  --white:#fff;
}
*{box-sizing:border-box;margin:0;padding:0}
html,body{width:1200px;height:3279px;overflow:hidden}
body{font-family:"Raleway",Arial,sans-serif;color:var(--text);background:var(--white);position:relative}
a{color:inherit;text-decoration:none}

.topbar{height:30px;background:var(--dark);color:var(--white);font-size:12px;font-weight:700;display:flex;justify-content:space-between;align-items:center;padding:0 87px}

.header{height:100px;display:flex;align-items:center;justify-content:space-between;padding:0 87px}
.brand{display:flex;align-items:center;gap:12px;font-size:22px;font-weight:700;color:var(--ink)}
.brand-mark{width:28px;height:28px;background:var(--red);border-radius:50%}
.nav{display:flex;gap:34px;font-size:11.5px;font-weight:600;color:var(--ink)}
.nav a.active{color:var(--red);border-bottom:2px solid var(--red);padding-bottom:6px}

.hero{position:relative;height:587px;background:linear-gradient(100deg,#3b3a3c 0%,#6b6260 45%,#9b8d84 75%,#5d5958 100%);color:var(--white)}
.hero-photo{position:absolute;inset:0}
.hero-copy{position:absolute;left:87px;top:170px;width:520px}
.hero-kicker{font-size:19px;font-weight:500;margin-bottom:8px}
.hero-title{font-size:46px;font-weight:800;line-height:1.05;margin-bottom:18px}
.hero-title span{color:var(--red)}
.hero-lead{font-size:14px;line-height:1.55;font-weight:500;margin-bottom:38px}
.btn{display:inline-flex;align-items:center;justify-content:center;height:44px;width:176px;border-radius:22px;font-size:13px;font-weight:700;letter-spacing:.3px}
.btn-red{background:var(--red);color:var(--white)}
.btn-ghost{border:2px solid var(--white);margin-left:26px}
.hero-arrow{position:absolute;top:400px;width:44px;height:44px;border-radius:50%;background:var(--white);display:flex;align-items:center;justify-content:center}
.hero-arrow.prev{left:20px}.hero-arrow.next{right:20px}
.dots{position:absolute;left:555px;top:682px;display:flex;gap:6px}
.dots i{width:18px;height:4px;background:var(--white)}
.dots i.on{background:var(--red)}

.features{position:absolute;top:770px;left:85px;display:flex;gap:24px}
.feature{width:326px;height:175px;border:1px solid var(--line);border-radius:4px;box-shadow:0 2px 8px rgba(0,0,0,.08);display:flex;gap:18px;padding:30px 22px}
.feature svg{flex:none;margin-top:10px}
.feature h3{font-size:18px;font-weight:700;color:var(--ink);margin-bottom:6px}
.feature p{font-size:13px;line-height:1.35}

.welcome{position:absolute;top:999px;left:0;width:1200px;height:398px;display:flex;background:var(--light)}
.welcome-photo{width:614px;height:398px;background:linear-gradient(135deg,#8fae73,#d8d4c8 50%,#6d5a4c)}
.welcome-body{padding:28px 60px 0 60px;width:586px}
.section-title{font-size:29px;font-weight:800;color:var(--ink);letter-spacing:.3px}
.section-title span{color:var(--red)}
.welcome-body p{font-size:13px;line-height:1.6;margin:14px 0 24px}
.welcome-body .btn{width:176px;height:42px}

.section-head{position:absolute;left:0;width:1200px;text-align:center}
.section-head p{font-size:14px;line-height:1.4;width:500px;margin:6px auto 0;color:var(--ink)}

.causes{position:absolute;top:1550px;left:85px;display:flex;gap:26px}
.cause{width:326px;height:378px;border:1px solid var(--line);box-shadow:0 1px 5px rgba(0,0,0,.06);text-align:center}
.cause-photo{height:180px;background:linear-gradient(135deg,#7fa35c,#d8d6cc 55%,#8f7a66)}
.cause h3{font-size:18px;font-weight:700;color:var(--ink);margin:34px 0 12px}
.cause p{font-size:13.5px;line-height:1.45;padding:0 22px}
.cause a{display:block;margin-top:26px;font-size:13px;font-weight:700;color:var(--green)}

.stats{position:absolute;top:1983px;left:0;width:1200px;height:192px;background:linear-gradient(90deg,#6f5a4e,#a08a77 50%,#5c4e46)}
.stat-row{position:absolute;top:32px;left:85px;display:flex;gap:26px}
.stat{width:240px;height:127px;background:rgba(25,20,18,.82);text-align:center;color:var(--white);padding-top:20px}
.stat b{display:block;font-size:40px;font-weight:800;color:var(--gold)}
.stat i{display:block;width:30px;height:3px;background:var(--white);margin:8px auto 10px}
.stat span{font-size:12px;font-weight:700}

.photos{position:absolute;top:2328px;left:85px;display:flex;gap:26px}
.photo{width:502px;height:208px;background:linear-gradient(135deg,#7fa35c,#dcd9cf 55%,#8b7766)}
.pager{position:absolute;top:2568px;left:551px;display:flex;gap:16px}
.pager span{width:40px;height:40px;border-radius:50%;background:#e6e6e6;display:flex;align-items:center;justify-content:center}

.map{position:absolute;top:2660px;left:0;width:1200px;height:304px;background:linear-gradient(120deg,#e8e5dc,#dfe6d4 50%,#d7e3cd)}

.footer{position:absolute;top:2964px;left:0;width:1200px;height:271px;padding:100px 85px 0;display:flex}
.footer h4{font-size:14px;font-weight:700;color:var(--ink);margin-bottom:22px;letter-spacing:.3px}
.col-address{width:352px}
.col-address li{list-style:none;font-size:13px;display:flex;align-items:center;gap:12px;margin-bottom:16px}
.col-sitemap{width:326px}
.sitemap{display:grid;grid-template-columns:128px 1fr;row-gap:13px;font-size:13px}
.col-find .search{display:flex;margin-bottom:16px}
.search span{width:230px;height:34px;border:1px solid #ccc;font-size:13px;color:#999;padding:8px 10px}
.search b{width:74px;height:34px;background:var(--red);color:var(--white);font-size:12px;display:flex;align-items:center;justify-content:center}
.social{display:flex;align-items:center;gap:10px;font-size:13px}
.social i{width:18px;height:18px;border-radius:50%;background:#3b5b99}
.copyright{position:absolute;top:3235px;left:0;width:1200px;height:44px;background:var(--dark);color:var(--white);font-size:13px;font-weight:600;display:flex;align-items:center;justify-content:center}
</style>
</head>
<body>

<div class="topbar"><span>Toll Free: (855) 410-2290</span><span>New York: 518-555-0183</span></div>

<header class="header">
  <a class="brand" href="#"><span class="brand-mark"></span>Harbor Kindness</a>
  <nav class="nav">
    <a class="active" href="#">Home</a><a href="#">Missions ▾</a><a href="#">Family ▾</a><a href="#">How it works</a><a href="#">About Us ▾</a><a href="#">Sponsors News</a><a href="#">Donate Wall of Needs</a>
  </nav>
</header>

<section class="hero">
  <div class="hero-photo" role="img" aria-label="Child at an orphan house receiving donated food"></div>
  <div class="hero-copy">
    <div class="hero-kicker">HARBOR KINDNESS</div>
    <h1 class="hero-title"><span>DONATED</span> TO ORPHAN HOUSE</h1>
    <p class="hero-lead">Lorem Ipsum has been the industry's standard dummy text ever since the, when an unknown printer took a galley of type and scrambled it to make a type specimen book.</p>
    <a class="btn btn-red" href="#">DONATE</a><a class="btn btn-ghost" href="#">READ MORE</a>
  </div>
  <a class="hero-arrow prev" href="#"><svg width="12" height="14" viewBox="0 0 12 14"><path d="M8 2 3 7l5 5" stroke="#e8262d" stroke-width="2.5" fill="none"/></svg></a>
  <a class="hero-arrow next" href="#"><svg width="12" height="14" viewBox="0 0 12 14"><path d="M4 2l5 5-5 5" stroke="#e8262d" stroke-width="2.5" fill="none"/></svg></a>
  <div class="dots"><i></i><i class="on"></i><i></i><i></i></div>
</section>

<section class="features">
  <div class="feature">
    <svg width="56" height="70" viewBox="0 0 56 70"><path d="M20 4h16l-5 12h-6z" fill="#333"/><path d="M22 18h12c14 10 20 24 18 38-2 10-10 12-24 12S6 66 4 56C2 42 8 28 22 18z" fill="#333"/><text x="28" y="56" font-size="26" font-weight="700" fill="#fff" text-anchor="middle" font-family="Arial">$</text></svg>
    <div><h3>DONATION</h3><p>It has survived not only five centuries, but also the leap into electronic typesetting, remaining.</p></div>
  </div>
  <div class="feature">
    <svg width="70" height="70" viewBox="0 0 70 70"><path d="M35 36C20 26 16 20 16 14a9 9 0 0 1 19-3 9 9 0 0 1 19 3c0 6-4 12-19 22z" fill="#333"/><path d="M2 50h12l14 4h14a4 4 0 0 1 0 8H26h18l18-10a4 4 0 0 1 4 6L46 68H2z" fill="#333"/></svg>
    <div><h3>FUNDRAISE</h3><p>It has survived not only five centuries, but also the leap into electronic typesetting, remaining.</p></div>
  </div>
  <div class="feature">
    <svg width="66" height="66" viewBox="0 0 66 66" fill="none" stroke="#333" stroke-width="3"><circle cx="20" cy="18" r="9"/><circle cx="46" cy="18" r="9"/><path d="M4 50c0-12 7-20 16-20s16 8 16 20zM30 50c0-12 7-20 16-20s16 8 16 20z"/><circle cx="33" cy="50" r="12" fill="#fff"/><path d="M33 56c-6-4-8-6-8-9a4 4 0 0 1 8-1 4 4 0 0 1 8 1c0 3-2 5-8 9z" fill="#333" stroke="none"/></svg>
    <div><h3>VOLUNTEERS</h3><p>It has survived not only five centuries, but also the leap into electronic typesetting, remaining.</p></div>
  </div>
</section>

<section class="welcome">
  <div class="welcome-photo" role="img" aria-label="Volunteers handing donated clothes to young children"></div>
  <div class="welcome-body">
    <h2 class="section-title">WELCOME &nbsp;TO <span>OUR CHARITY</span></h2>
    <p>Harbor Kindness is a non-profit organization that was created for one purpose: helping the less fortunate in our country's time of greatest need. Started in 2007, Harbor Kindness has been a dedicated member of its local communities over the past four years. The company's clothing collection efforts have allowed it to provide some of the neediest members of the community to clothe themselves and their families. The company's goal is to ensure that some of the most basic needs of the community's members are met thru the philanthropic efforts of the organizations members and contributors.</p>
    <a class="btn btn-red" href="#">READ MORE</a>
  </div>
</section>

<div class="section-head" style="top:1444px">
  <h2 class="section-title">RECENT <span>CAUSES</span></h2>
  <p>There are many variations of passages of Lorem Ipsum available, but the majority have suffered alteration.</p>
</div>

<section class="causes">
  <article class="cause"><div class="cause-photo" role="img" aria-label="Volunteer with children outdoors"></div><h3>THERE ARE MANY</h3><p>There are many variations of passages of Lorem Ipsum available, but the majority have suffered alteration.</p><a href="#">READ MORE</a></article>
  <article class="cause"><div class="cause-photo" role="img" aria-label="Volunteer with children outdoors"></div><h3>HELP DISASTER VICTIMS</h3><p>There are many variations of passages of Lorem Ipsum available, but the majority have suffered alteration.</p><a href="#">READ MORE</a></article>
  <article class="cause"><div class="cause-photo" role="img" aria-label="Volunteer with children outdoors"></div><h3>WE ARE A TRUE</h3><p>There are many variations of passages of Lorem Ipsum available, but the majority have suffered alteration.</p><a href="#">READ MORE</a></article>
</section>

<section class="stats" role="img" aria-label="Blurred background photo of a donation event">
  <div class="stat-row">
    <div class="stat"><b>2,145</b><i></i><span>HELP</span></div>
    <div class="stat"><b>845</b><i></i><span>DONATION CAMP</span></div>
    <div class="stat"><b>681</b><i></i><span>VOLUNTEERS</span></div>
    <div class="stat"><b>1,985</b><i></i><span>HAPPY PEOPLE</span></div>
  </div>
</section>

<div class="section-head" style="top:2220px">
  <h2 class="section-title">RECENT <span>PHOTOS</span></h2>
  <p>There are many variations of passages of Lorem Ipsum available, but the majority have suffered alteration.</p>
</div>

<section class="photos">
  <div class="photo" role="img" aria-label="Volunteer sharing donations with children"></div>
  <div class="photo" role="img" aria-label="Volunteer sharing donations with children"></div>
</section>
<div class="pager">
  <span><svg width="10" height="12" viewBox="0 0 10 12"><path d="M7 1 2 6l5 5" stroke="#555" stroke-width="2" fill="none"/></svg></span>
  <span><svg width="10" height="12" viewBox="0 0 10 12"><path d="M3 1l5 5-5 5" stroke="#555" stroke-width="2" fill="none"/></svg></span>
</div>

<section class="map" role="img" aria-label="Regional map marking local donation drop-off locations"></section>

<footer class="footer">
  <div class="col-address">
    <h4>ADDRESS</h4>
    <ul>
      <li><svg width="12" height="12" viewBox="0 0 12 12"><path d="M2 1h3l1 3-2 1a7 7 0 0 0 3 3l1-2 3 1v3c-6 0-10-4-9-9z" fill="#333"/></svg>(855) 410-2290</li>
      <li><svg width="12" height="10" viewBox="0 0 12 10"><rect x=".5" y=".5" width="11" height="9" fill="none" stroke="#333"/><path d="M1 1l5 4 5-4" fill="none" stroke="#333"/></svg>hello@harborkindness.org</li>
      <li><svg width="10" height="13" viewBox="0 0 10 13"><path d="M5 12C1 7 1 5 1 4.5a4 4 0 0 1 8 0C9 5 9 7 5 12z" fill="#333"/><circle cx="5" cy="4.5" r="1.5" fill="#fff"/></svg>27 Lantern Hill Road, Millbrook, NY 12545</li>
    </ul>
  </div>
  <div class="col-sitemap">
    <h4>SITE MAP</h4>
    <div class="sitemap"><a href="#">Home</a><a href="#">About Us</a><a href="#">Missions</a><a href="#">Sponsors News</a><a href="#">Family</a><a href="#">Donate Wall of Needs</a><a href="#">How it works</a></div>
  </div>
  <div class="col-find">
    <h4>FIND LOCAL DONATION PLACE</h4>
    <div class="search"><span>Zip</span><b>SEARCH</b></div>
    <a class="social" href="#"><i></i>Social page</a>
  </div>
</footer>
<div class="copyright">© 2018 Harbor Kindness. All Rights Reserved</div>

</body>
</html>
```